Business Card, T Shirt ,Fax cover, Letterhead, Invoice
Kovac Painting & Decorating
Professional
Tobias Kovac
Bay no 482, 67 North Amber Way SW
California AB T3K5M8
tobias@kovacpaintworx.com
www.kovacpaintworx.com
Contents of the Invoice

```html
<!DOCTYPE html>
<html lang="en">
<head>
<meta charset="utf-8">
<title>Kovac Painting &amp; Decorating – Business Cards</title>
<link rel="stylesheet" href="https://fonts.googleapis.com/css2?family=Open+Sans:wght@400;700;800&family=Noto+Serif:wght@700&display=swap">
<style>
  :root{
    --bg:#e4e2de;
    --card:#ffffff;
    --green:#3b8a2e;
    --green-dark:#2a6a22;
    --green-light:#6fb544;
    --orange:#ef6a1c;
    --orange-light:#f7a13a;
    --orange-dark:#e2521a;
    --text:#555555;
  }
  *{box-sizing:border-box;margin:0;padding:0}
  html,body{width:1200px;height:833px;overflow:hidden}
  body{background:var(--bg);font-family:"Open Sans",Arial,sans-serif;position:relative}
  .card{position:absolute;width:438px;height:288px;box-shadow:0 3px 10px rgba(0,0,0,.25);overflow:hidden}
  .front-a{left:149px;top:144px}
  .front-b{left:632px;top:144px}
  .back-green{left:149px;top:497px}
  .back-orange{left:632px;top:497px}
  .front{background:linear-gradient(180deg,#ffffff 0%,#f1f1f1 100%)}
  .stripe{position:absolute;left:0;right:0;bottom:0;height:20px;background:var(--green);border-top:4px solid var(--orange)}
  .person{font-family:"Noto Serif",Georgia,serif;font-weight:700;color:var(--green);font-size:17px;position:absolute}
  .brand{position:absolute;display:flex;align-items:center;gap:8px}
  .brand-dot{width:30px;height:30px;border-radius:50%;background:var(--orange);flex:none}
  .brand-name{font-weight:800;color:var(--green);font-size:12px;line-height:1.2;width:120px}
  .contact{position:absolute;list-style:none;font-size:9.5px;color:var(--text);line-height:13.5px}
  .contact li{display:flex;align-items:flex-start;gap:6px}
  .contact svg{flex:none;margin-top:3px}
  .contact .gap{margin-top:5px}
  .front-a .person{left:22px;top:54px}
  .front-a .brand{left:22px;top:126px}
  .front-a .contact{left:246px;top:90px}
  .front-b .brand{left:22px;top:26px}
  .front-b .person{left:62px;top:124px}
  .front-b .contact{left:246px;top:118px}
  .back{display:flex;flex-direction:column;align-items:center;justify-content:center;color:#fff;text-align:center}
  .back-green{background:radial-gradient(circle at 50% 45%,var(--green-light) 0%,var(--green) 55%,var(--green-dark) 100%)}
  .back-orange{background:radial-gradient(circle at 50% 45%,var(--orange-light) 0%,var(--orange) 55%,var(--orange-dark) 100%)}
  .back-dot{width:52px;height:52px;border-radius:50%;background:#fff;margin-bottom:16px}
  .back-name{font-weight:700;font-size:12px;letter-spacing:.3px}
  .back-web{font-weight:700;font-size:11px;margin-top:3px}
</style>
</head>
<body>

<section class="card front front-a">
  <h2 class="person">Tobias Kovac</h2>
  <div class="brand"><span class="brand-dot"></span><span class="brand-name">Kovac Painting &amp; Decorating</span></div>
  <ul class="contact">
    <li><svg width="8" height="8" viewBox="0 0 8 8"><path d="M4 0C2.3 0 1 1.3 1 3c0 2.2 3 5 3 5s3-2.8 3-5C7 1.3 5.7 0 4 0z" fill="var(--green)"/></svg><span>Bay no 482, 67 North Amber Way SW<br>California AB T3K5M8</span></li>
    <li class="gap"><svg width="8" height="8" viewBox="0 0 8 8"><rect x="1.5" y="0" width="5" height="8" rx="1" fill="var(--green)"/></svg>403 555 0142</li>
    <li><svg width="8" height="8" viewBox="0 0 8 8"><rect x="1.5" y="0" width="5" height="8" rx="1" fill="var(--green)"/></svg>423 555 0187</li>
    <li><svg width="8" height="8" viewBox="0 0 8 8"><rect x="1.5" y="0" width="5" height="8" rx="1" fill="var(--green)"/></svg>423 555 0163</li>
    <li><svg width="8" height="8" viewBox="0 0 8 8"><rect x="0" y="1.5" width="8" height="5" fill="var(--green)"/></svg>tobias@kovacpaintworx.com</li>
    <li><svg width="8" height="8" viewBox="0 0 8 8"><circle cx="4" cy="4" r="3.5" fill="var(--green)"/></svg>www.kovacpaintworx.com</li>
  </ul>
  <div class="stripe"></div>
</section>

<section class="card front front-b">
  <div class="brand"><span class="brand-dot"></span><span class="brand-name">Kovac Painting &amp; Decorating</span></div>
  <h2 class="person">Tobias Kovac</h2>
  <ul class="contact">
    <li><svg width="8" height="8" viewBox="0 0 8 8"><path d="M4 0C2.3 0 1 1.3 1 3c0 2.2 3 5 3 5s3-2.8 3-5C7 1.3 5.7 0 4 0z" fill="var(--green)"/></svg><span>Bay no 482, 67 North Amber Way SW<br>California AB T3K5M8</span></li>
    <li class="gap"><svg width="8" height="8" viewBox="0 0 8 8"><rect x="1.5" y="0" width="5" height="8" rx="1" fill="var(--green)"/></svg>403 555 0142</li>
    <li><svg width="8" height="8" viewBox="0 0 8 8"><rect x="1.5" y="0" width="5" height="8" rx="1" fill="var(--green)"/></svg>423 555 0187</li>
    <li><svg width="8" height="8" viewBox="0 0 8 8"><rect x="1.5" y="0" width="5" height="8" rx="1" fill="var(--green)"/></svg>423 555 0163</li>
    <li><svg width="8" height="8" viewBox="0 0 8 8"><rect x="0" y="1.5" width="8" height="5" fill="var(--green)"/></svg>tobias@kovacpaintworx.com</li>
    <li><svg width="8" height="8" viewBox="0 0 8 8"><circle cx="4" cy="4" r="3.5" fill="var(--green)"/></svg>www.kovacpaintworx.com</li>
  </ul>
  <div class="stripe"></div>
</section>

<section class="card back back-green">
  <span class="back-dot"></span>
  <p class="back-name">KOVAC PAINTING &amp; DECORATING</p>
  <p class="back-web">www.kovacpaintworx.com</p>
</section>

<section class="card back back-orange">
  <span class="back-dot"></span>
  <p class="back-name">KOVAC PAINTING &amp; DECORATING</p>
  <p class="back-web">www.kovacpaintworx.com</p>
</section>

</body>
</html>
```